Need effective Landing Page for product and service

Need help re-designing landing page:

Our company (in New York) offers upgrades to homes to make them more efficient, save energy and reduce utility bills. We do not do, or suggest every possible measure, like sealing and insulating a home, replacing windows, etc. We only offer high efficiency Ductless Mini Split Systems.

The landing page is to introduce the idea, and get people to fill the form. We already running a page at www.breezlotech.net, but it is dull and boring, while it must be exciting, creating an urge to fill the form (schedule live consultation).

Visitors get to the page from Facebook Ad, designer must make sure there is congruence between the ad and the page.

Industry/Entity Type

Product

```html
<!DOCTYPE html>
<html lang="en">
<head>
<meta charset="utf-8">
<title>Airvale Comfort Solutions – Ductless Heat Pumps</title>
<link href="https://fonts.googleapis.com/css2?family=Lato:ital,wght@0,400;0,700;0,900;1,400;1,700&display=swap" rel="stylesheet">
<style>
:root{
  --navy:#0c2a55;
  --navy-deep:#081d3d;
  --blue:#1d4f8f;
  --blue-bright:#2a6bb8;
  --link-blue:#1f5fa8;
  --yellow:#f6c93a;
  --yellow-soft:#fbdc6d;
  --yellow-deep:#e7b21c;
  --ink:#1d2430;
  --grey-text:#5d6470;
  --muted-blue:#9db3cf;
  --pale:#e6ebf2;
  --white:#ffffff;
  --grass:#5fae2c;
}
*{box-sizing:border-box;margin:0;padding:0}
html,body{width:1200px;height:2777px;overflow:hidden}
body{font-family:'Lato',Arial,sans-serif;color:var(--ink);background:var(--white)}
.wrap{width:944px;margin:0 auto;position:relative}

/* hero */
.hero{height:657px;position:relative;overflow:hidden;
  background:linear-gradient(180deg,var(--navy) 0%,var(--blue) 62%,#f4d45a 80%,var(--yellow) 100%)}
.hero::after{content:"";position:absolute;left:50%;top:330px;width:900px;height:400px;margin-left:-100px;
  background:radial-gradient(ellipse at center,rgba(255,240,170,.55),rgba(255,240,170,0) 65%)}
.topbar{height:90px;display:flex;align-items:center;justify-content:space-between;position:relative;z-index:2}
.brand{display:flex;align-items:center;gap:10px;font-weight:900;font-size:30px;color:var(--yellow)}
.brand-dot{width:18px;height:18px;border-radius:50%;background:var(--yellow)}
.nav{display:flex;gap:28px;font-size:14px;text-transform:uppercase;letter-spacing:.3px}
.nav a{color:var(--white);text-decoration:none;padding-bottom:6px}
.nav a.active{border-bottom:2px solid var(--white);font-weight:700}
.hero-copy{position:relative;z-index:2;width:560px;margin-top:58px}
.hero h1{font-size:46px;font-weight:900;color:var(--yellow);line-height:1.1}
.hero h2{font-size:26px;font-weight:700;color:var(--white);line-height:1.25;margin-top:14px}
.hero p{font-size:13px;line-height:1.55;color:var(--muted-blue);margin-top:22px;width:520px}
.hero-product{position:absolute;right:0;top:150px;width:360px;height:340px;z-index:2;border-radius:6px;
  background:linear-gradient(160deg,#f4f7fb,#c9d6e6 55%,#8fa6c3)}
.checks{position:absolute;z-index:2;top:510px;left:0;list-style:none}
.checks li{display:flex;align-items:center;gap:14px;font-size:19px;font-weight:700;color:var(--ink);margin-bottom:14px}
.checks svg{width:28px;height:28px;flex:none}

/* benefits */
.benefits{height:613px;padding-top:46px}
.benefits h3{text-align:center;font-size:30px;font-weight:700;color:var(--navy)}
.cols{display:flex;gap:36px;margin-top:32px}
.col{width:290px}
.col .pic{height:186px;width:100%}
.pic-house{background:linear-gradient(180deg,#7fb4e8,#a9cfe9 50%,#6e9a4b)}
.pic-air{background:radial-gradient(circle at 50% 45%,#cfe6ff,#4d87cf 55%,#173d7a)}
.pic-family{background:linear-gradient(135deg,#f0c7a0,#c98f62 55%,#6e8fb8)}
.col h4{font-size:22px;font-weight:700;color:var(--link-blue);margin-top:26px}
.col p{font-size:13px;line-height:1.5;color:var(--grey-text);margin-top:10px}

/* testimonials */
.testimonials{height:330px;background:var(--pale);padding-top:52px;position:relative}
.testimonials h3{font-size:25px;font-weight:700;color:var(--ink)}
.quotes{display:flex;justify-content:space-between;margin-top:34px}
.quote{width:444px;background:var(--white);border:2px solid #c5cfdc;border-radius:10px;padding:22px 34px;
  font-size:14px;font-weight:700;line-height:1.45;color:var(--ink);position:relative}
.quote::before{content:"";position:absolute;left:-2px;top:40px;width:2px;height:30px;background:var(--white)}
.grass{position:absolute;left:0;right:0;bottom:-30px;height:60px;z-index:2;
  background:linear-gradient(180deg,rgba(95,174,44,0) 0%,#7cc33e 40%,#3f8a1f 100%)}

/* contact */
.contact{height:888px;background:radial-gradient(ellipse at 50% 35%,var(--blue),var(--navy) 60%,var(--navy-deep));padding-top:62px}
.contact h3{font-size:38px;font-weight:900;color:var(--yellow)}
.contact .lead{font-size:16px;line-height:1.45;color:var(--white);margin-top:12px;width:640px}
.contact-grid{display:flex;gap:60px;margin-top:50px}
.form{width:471px;height:486px;background:var(--yellow);padding:0 32px;position:relative}
.form h5{font-size:22px;font-weight:700;color:var(--ink);height:84px;display:flex;align-items:center;
  border-bottom:1px solid rgba(0,0,0,.12);margin:0 -32px;padding:0 32px;background:var(--yellow-deep)}
.field{background:var(--white);border-radius:6px;height:50px;margin-top:16px;padding:15px 18px;font-size:14px;font-weight:700;color:var(--ink)}
.field.area{height:130px}
.note{font-size:11px;color:var(--ink);margin-top:12px}
.submit-row{display:flex;align-items:center;gap:22px;margin-top:20px}
.submit{width:144px;height:50px;border-radius:6px;background:var(--yellow-soft);border:1px solid var(--yellow-deep);
  font-size:18px;font-weight:900;color:var(--ink);display:flex;align-items:center;justify-content:center}
.submit-row span{font-size:18px;font-weight:700;color:var(--ink)}
.perks{width:413px}
.perk{display:flex;gap:20px;margin-bottom:48px}
.perk .pic{width:80px;height:80px;border-radius:50%;flex:none;margin-top:6px}
.pic-breeze{background:radial-gradient(circle at 40% 35%,#bde8ff,#2c9ad8 55%,#0b5f8c)}
.pic-remote{background:radial-gradient(circle at 40% 35%,#ffffff,#c8d1dc 60%,#8a97a8)}
.perk h6{font-size:17px;font-weight:900;color:var(--yellow);text-transform:uppercase;letter-spacing:.3px}
.perk p{font-size:12px;line-height:1.5;color:var(--muted-blue);margin-top:8px}
.callbox{width:500px;margin:30px auto 0;border:3px solid var(--yellow);border-radius:10px;background:var(--navy);
  padding:22px 0;text-align:center;font-size:26px;font-weight:900;color:var(--yellow);line-height:1.3;position:relative}
.callbox svg{position:absolute;left:50%;top:-20px;margin-left:-18px}

/* closing */
.closing{height:172px;background:var(--pale);display:flex;align-items:center;justify-content:center;
  text-align:center;font-size:27px;line-height:1.35;color:var(--ink)}
.footer{height:77px;display:flex;align-items:center}
.footer .wrap{display:flex;justify-content:space-between;font-size:12px;color:var(--grey-text)}
</style>
</head>
<body>

<header class="hero">
  <div class="wrap">
    <div class="topbar">
      <div class="brand"><span class="brand-dot"></span>Airvale</div>
      <nav class="nav">
        <a class="active" href="#">Ductless A/C &amp; Heat Pumps</a>
        <a href="#">Testimonials</a>
        <a href="#">Installations</a>
        <a href="#">About us</a>
      </nav>
    </div>
    <div class="hero-copy">
      <h1>Is your Home Efficient?</h1>
      <h2>Become GREEN! Get High Efficiency Ductless HEAT and COOL System and Save Money</h2>
      <p>Set yourself free from high energy costs. Create a more comfortable, energy efficient home and cut your energy bills by hundreds, or even more every year by upgrading your home heating and cooling system. Home heating and cooling expenses account for about 50% of total monthly energy bills. This was researched by several independent studies. Cutting energy bills by improving your home performance is one of the ways to become GREEN - save wasted resources and reduce environmental impact.</p>
    </div>
    <div class="hero-product" role="img" aria-label="Ductless mini split indoor unit with outdoor condenser and remote"></div>
    <ul class="checks">
      <li><svg viewBox="0 0 28 28"><circle cx="14" cy="14" r="13" fill="#0c2a55"/><path d="M8 14.5l4 4 8-9" stroke="#f6c93a" stroke-width="3" fill="none" stroke-linecap="round" stroke-linejoin="round"/></svg>Reduce wasted energy - heat pumps are 30% more efficient</li>
      <li><svg viewBox="0 0 28 28"><circle cx="14" cy="14" r="13" fill="#0c2a55"/><path d="M8 14.5l4 4 8-9" stroke="#f6c93a" stroke-width="3" fill="none" stroke-linecap="round" stroke-linejoin="round"/></svg>Improve the quality of air you and your family breathes</li>
      <li><svg viewBox="0 0 28 28"><circle cx="14" cy="14" r="13" fill="#0c2a55"/><path d="M8 14.5l4 4 8-9" stroke="#f6c93a" stroke-width="3" fill="none" stroke-linecap="round" stroke-linejoin="round"/></svg>Stop fighting over "who has the control"</li>
    </ul>
  </div>
</header>

<section class="benefits">
  <div class="wrap">
    <h3>Gain better control of your energy bills, improve comfort and health!</h3>
    <div class="cols">
      <article class="col">
        <div class="pic pic-house" role="img" aria-label="Suburban family house under a blue sky"></div>
        <h4>Reduce wasted energy</h4>
        <p>Ductless heat pumps are 30% more efficient than any other type of heating system. Heat pumps do not "burn" any fossil fuel, like gas or oil. Even though they use electricity to run, heat pumps do not "convert" electric power to heat, like an electric heater. Heat pumps use electric power only to "deliver" (or "pump") the heat taken from nature, and there is plenty of "free" heat outside of your home. Green, isn't it?</p>
      </article>
      <article class="col">
        <div class="pic pic-air" role="img" aria-label="Swirl of fresh clean air on blue"></div>
        <h4>Improve air quality</h4>
        <p>Ductless Systems do not use duct to distribute air. They are duct-less! In turn, no ducts means no dust, no bacteria, no odor. Conventional central systems utilize ducts which take space in your home, and well known for collecting lots of dust which is excellent breeding environment for dust mites and other creepy creatures you do not want your family to breathe.</p>
      </article>
      <article class="col">
        <div class="pic pic-family" role="img" aria-label="Happy family smiling together"></div>
        <h4>Who has the control?</h4>
        <p>Everyone! Ductless heat pump systems let you have total control, which means ultimate comfort. Remember saying: "I want the whole house to be the same temperature"? Why? Are your children comfortable where you are? Does your living room need much heat at night, or kitchen when you cook? The Ductless system cranks up heat where needed, and reduces power where not needed, thus using less energy to achieve the same results.</p>
      </article>
    </div>
  </div>
</section>

<section class="testimonials">
  <div class="wrap">
    <h3>Testimonials</h3>
    <div class="quotes">
      <blockquote class="quote">"I appreciated the explanation and communication about what needed to be done. Installation team took special care and attention to assure that my new ductless heat pump system was installed properly. Product specialist gave good product advice. I am very happy."</blockquote>
      <blockquote class="quote">"I am extremely happy with my new ductless system. My girlfriends have had a tour of the installation and said it was awesome. If I could only show it to everyone. Thank you for great product and highest quality of installation, and pass on my highest regard and complete satisfaction"...</blockquote>
    </div>
  </div>
  <div class="grass" role="img" aria-label="Strip of green grass"></div>
</section>

<section class="contact">
  <div class="wrap">
    <h3>Ready for more information?</h3>
    <p class="lead">Talk to live consultant (he knows much more than we can possibly place on this page), and get $500 discount coupon (in case you decide to upgrade your home)</p>
    <div class="contact-grid">
      <form class="form">
        <h5>Yes, schedule my FREE consultation</h5>
        <div class="field">Enter your name *</div>
        <div class="field">Enter email address *</div>
        <div class="field area">Enter comments or questions</div>
        <p class="note">Your information will not be shared, we promise!</p>
        <div class="submit-row"><div class="submit">SUBMIT</div><span>and print $500 coupon</span></div>
      </form>
      <div class="perks">
        <div class="perk">
          <div class="pic pic-breeze" role="img" aria-label="Tropical beach with palm tree"></div>
          <div>
            <h6>Quiet like sea breeze</h6>
            <p>Both the outdoor and indoor units operate extremely quietly. The indoor units operate quieter than a human whisper, as low as 19dBs. Outdoor units operate as low as 46dBs, that is quieter than a refrigerator, whereas your neighbors having a traditional central heat pump units that run at around 75dBs, which is equivalent to heavy traffic or a vacuum cleaner.</p>
          </div>
        </div>
        <div class="perk">
          <div class="pic pic-remote" role="img" aria-label="Hand holding a wireless remote controller"></div>
          <div>
            <h6>Smart controller</h6>
            <p>Controlling your comfort is easy. Just use the smart remote controller to get your perfect temperature with the touch of a button. Choose mode of operation between COOL, HEAT, DRY or AUTO. AUTO mode will automatically decide if you need cooling or heating delivered to the space to maintain the set temperature. Everything you need to control your comfort is right there in your room with you; not in another room or a different floor.</p>
          </div>
        </div>
      </div>
    </div>
    <div class="callbox">
      <svg width="36" height="20" viewBox="0 0 36 20"><path d="M0 20L18 2 36 20" fill="#0c2a55" stroke="#f6c93a" stroke-width="3"/></svg>
      or call toll free 888.555.0142<br>we are open Mon - Fri 8am - 5pm
    </div>
  </div>
</section>

<section class="closing">
  <p>Increasing energy efficiency is a great way to reduce strain<br>on natural resources and save money.</p>
</section>

<footer class="footer">
  <div class="wrap">
    <span>Airvale Comfort Solutions, 2150 Linden Ave, Queens, NY 11385, phone 888 555 0142</span>
    <span>Copyright © Airvale Comfort Solutions</span>
  </div>
</footer>

</body>
</html>
```